Maple Hollow Bloom Panels Business card

Looking to have a business card design incorporating my logo for my flower wall business.

Industry/Entity Type

Wedding & event planning

Contact Information for Business Card

My business logo, my name - Lena Whitcombe (owner), my tagline - Let us add your finishing bloom, phone # 401-726-3148, email address - maplehollowbloompanels@mailvane.net, my website - maplehollowbloompanels.net, Instagram handle- @maplehollowbloompanels, FB handle Handle - maplehollowbloompanels

Font styles to use
Other font styles liked:
• Sentaina is the font that is used in my logo

Requirements
Must have
• Would like a double sided business card

```html
<!DOCTYPE html>
<html lang="en">
<head>
<meta charset="utf-8">
<title>Maple Hollow Bloom Panels – Business Card</title>
<link href="https://fonts.googleapis.com/css2?family=Alegreya:ital,wght@0,400;0,500;1,400&display=swap" rel="stylesheet">
<style>
  :root {
    --page: #f4eef0;
    --sand: #e3d6bd;
    --paper: #ffffff;
    --magenta: #9c1f86;
    --magenta-soft: #a5579a;
    --mauve: #b997ae;
    --ink: #2b2b2b;
    --icon-bg: #efe6da;
  }
  * { box-sizing: border-box; margin: 0; padding: 0; }
  html, body { width: 1200px; height: 1200px; overflow: hidden; }
  body {
    background: var(--page);
    font-family: "Alegreya", Georgia, serif;
    position: relative;
  }
  .card {
    position: absolute;
    left: 180px;
    width: 840px;
    height: 480px;
    overflow: hidden;
    box-shadow: 0 6px 18px rgba(80, 50, 70, 0.18);
  }
  .card--front { top: 90px; background: var(--sand); }
  .card--back { top: 630px; background: var(--mauve); }

  .front-shape { position: absolute; inset: 0; }

  .brand-name {
    position: absolute;
    left: 70px; top: 92px;
    font-size: 30px;
    line-height: 1.1;
    white-space: nowrap;
    color: var(--ink);
    font-weight: 400;
  }
  .owner-name {
    position: absolute;
    left: 84px; top: 178px;
    font-size: 42px;
    line-height: 1.1;
    color: var(--magenta);
    font-weight: 400;
  }
  .owner-role {
    position: absolute;
    left: 86px; top: 230px;
    font-size: 21px;
    letter-spacing: 1px;
    color: var(--magenta-soft);
  }
  .bloom-art {
    position: absolute;
    border-radius: 50%;
    background: radial-gradient(circle at 45% 40%, #a52a8e 0%, #9c1f86 55%, rgba(156,31,134,0) 72%);
  }
  .bloom-art--left { left: 70px; top: 280px; width: 220px; height: 180px; }
  .bloom-art--right { left: 520px; top: 40px; width: 190px; height: 190px; }

  .contact-list {
    position: absolute;
    left: 430px; top: 228px;
    list-style: none;
  }
  .contact-item {
    display: flex;
    align-items: center;
    height: 38px;
    font-size: 17px;
    color: var(--ink);
  }
  .contact-icon {
    width: 26px; height: 26px;
    margin-right: 18px;
    flex: none;
    display: flex; align-items: center; justify-content: center;
  }
  .contact-icon svg { width: 26px; height: 26px; }

  .tagline {
    position: absolute;
    top: 34px; left: 0; right: 0;
    text-align: center;
    font-size: 32px;
    color: var(--paper);
    font-weight: 400;
  }
  .emblem {
    position: absolute;
    left: 285px; top: 110px;
    width: 270px; height: 270px;
    border-radius: 50%;
    background: var(--paper);
    display: flex; align-items: center; justify-content: center;
    text-align: center;
  }
  .emblem-name {
    font-size: 30px;
    line-height: 1.15;
    color: var(--ink);
    width: 200px;
  }
</style>
</head>
<body>

<section class="card card--front" aria-label="Business card front">
  <svg class="front-shape" viewBox="0 0 840 480" preserveAspectRatio="none" aria-hidden="true">
    <path fill="#ffffff" d="M0 110 C60 60 180 80 280 90 C360 95 430 70 500 55 C560 40 640 20 720 40 C780 55 790 95 820 110 C845 130 830 170 810 190 C790 220 830 260 835 300 C840 350 790 360 720 370 C650 380 560 420 470 440 C420 450 400 420 380 380 C360 330 320 400 280 430 C240 460 170 470 110 455 C60 440 20 400 25 350 C30 300 0 260 0 220 Z"/>
  </svg>

  <h1 class="brand-name">Maple Hollow Bloom Panels</h1>
  <p class="owner-name">Lena Whitcombe</p>
  <p class="owner-role">OWNER</p>

  <div class="bloom-art bloom-art--left" role="img" aria-label="Illustration of two magenta peony blooms on thin stems"></div>
  <div class="bloom-art bloom-art--right" role="img" aria-label="Illustration of a large magenta peony bloom with a leaf"></div>

  <ul class="contact-list">
    <li class="contact-item">
      <span class="contact-icon">
        <svg viewBox="0 0 26 26" aria-hidden="true"><circle cx="13" cy="13" r="13" fill="var(--icon-bg)"/><path d="M9 7 L11 7 L12 10 L10.5 11.2 C11.3 13 12.8 14.6 14.8 15.5 L16 14 L19 15 L19 17 C19 18 18 19 17 19 C12 18.6 7.4 14 7 9 C7 8 8 7 9 7 Z" fill="var(--magenta)"/></svg>
      </span>
      # 401-726-3148
    </li>
    <li class="contact-item">
      <span class="contact-icon">
        <svg viewBox="0 0 26 26" aria-hidden="true"><circle cx="13" cy="13" r="13" fill="var(--icon-bg)"/><rect x="6.5" y="8.5" width="13" height="9" fill="none" stroke="var(--magenta)" stroke-width="1.3"/><path d="M6.5 8.5 L13 13.5 L19.5 8.5" fill="none" stroke="var(--magenta)" stroke-width="1.3"/></svg>
      </span>
      maplehollowbloompanels@mailvane.net
    </li>
    <li class="contact-item">
      <span class="contact-icon">
        <svg viewBox="0 0 26 26" aria-hidden="true"><circle cx="13" cy="13" r="13" fill="var(--icon-bg)"/><circle cx="13" cy="13" r="6.5" fill="none" stroke="var(--magenta)" stroke-width="1.2"/><ellipse cx="13" cy="13" rx="3" ry="6.5" fill="none" stroke="var(--magenta)" stroke-width="1"/><path d="M6.5 13 H19.5" stroke="var(--magenta)" stroke-width="1"/></svg>
      </span>
      maplehollowbloompanels.net
    </li>
    <li class="contact-item">
      <span class="contact-icon">
        <svg viewBox="0 0 26 26" aria-hidden="true"><rect x="1" y="1" width="24" height="24" rx="3" fill="var(--magenta)"/></svg>
      </span>
      @maplehollowbloompanels
    </li>
    <li class="contact-item">
      <span class="contact-icon">
        <svg viewBox="0 0 26 26" aria-hidden="true"><circle cx="13" cy="13" r="12" fill="var(--magenta)"/></svg>
      </span>
      maplehollowbloompanels
    </li>
  </ul>
</section>

<section class="card card--back" aria-label="Business card back">
  <p class="tagline">Let us add your finishing bloom</p>
  <div class="emblem">
    <p class="emblem-name">Maple Hollow Bloom Panels</p>
  </div>
</section>

</body>
</html>
```